Include the Cairnfield Guidance Academy Logo (attached) on EVERY design.
Paperback Workbook cover design will accompany attached:The Compass and The Climber; make your design fit with collection by using the same font and drop shadow
Clean, sharp, modern, design
Mountain in background is a nice touch almost "watermark like" to mimic attached logo
Provide 5 different color option backgrounds
Our organization is called Cairnfield Executive Coaching. We help clients reach their summit/goals as actual sherpas help mountain climbers reach the summit. See our website for more info www.cairnfieldguide.example

Target Market(s)

30 - 60 yr old men and women; Professional University Adult Continuing Education

Industry/Entity Type

Education

Requirements
Must have
• Cairnfield Guidance Academy logo included; Crew Captain Onboarding Course Workbook words included
• Provided several color background options
• Use The Compass and The Climber as inspiration, use same font and size specs
• This is a paperback book cover
Nice to have
• Mountain theme there but not focus

```html
<!DOCTYPE html>
<html lang="en">
<head>
<meta charset="utf-8">
<title>Crew Captain Onboarding Course Workbook</title>
<link rel="stylesheet" href="https://fonts.googleapis.com/css2?family=Cormorant+SC:wght@600;700&display=swap">
<style>
  :root {
    --paper: #f8fdec;
    --ink: #36373a;
    --brand-grey: #7b7d72;
    --brand-blue: #1f6aa5;
    --tone-light: #d6a66e;
    --tone-mid: #a8400f;
    --tone-deep: #4b1622;
    --tone-night: #2a0f2e;
  }
  * { margin: 0; padding: 0; box-sizing: border-box; }
  html, body { width: 1200px; height: 810px; overflow: hidden; background: var(--paper); }
  .cover {
    position: relative;
    width: 1200px;
    height: 810px;
    background: var(--paper);
    overflow: hidden;
    font-family: "Cormorant SC", "Times New Roman", serif;
  }
  .artwork-area {
    position: absolute;
    left: 0;
    top: 430px;
    width: 1200px;
    height: 380px;
    background: linear-gradient(180deg, var(--tone-light) 0%, var(--tone-mid) 35%, var(--tone-deep) 72%, var(--tone-night) 100%);
  }
  .brand {
    position: absolute;
    left: 916px;
    top: 60px;
    display: flex;
    align-items: flex-start;
    gap: 8px;
  }
  .brand-mark {
    width: 40px;
    height: 40px;
    margin-top: 14px;
    background: var(--brand-blue);
  }
  .brand-name {
    color: var(--brand-grey);
    font-weight: 600;
    font-size: 23px;
    line-height: 20px;
    letter-spacing: 0.5px;
  }
  .title-block {
    position: absolute;
    left: 666px;
    top: 170px;
    width: 500px;
    text-align: center;
    color: var(--ink);
  }
  .title-main {
    font-weight: 700;
    font-size: 60px;
    line-height: 78px;
    letter-spacing: 2px;
  }
  .title-sub {
    margin-top: 2px;
    font-weight: 600;
    font-size: 44px;
    line-height: 56px;
    letter-spacing: 2px;
  }
</style>
</head>
<body>
  <main class="cover">
    <div class="artwork-area" role="img" aria-label="Low-poly mountain range illustration in tan, rust and deep maroon tones"></div>

    <div class="brand">
      <span class="brand-mark"></span>
      <p class="brand-name">Cairnfield<br>Guidance<br>Academy</p>
    </div>

    <header class="title-block">
      <h1 class="title-main">Crew Captain<br>Onboarding</h1>
      <p class="title-sub">Course Workbook</p>
    </header>
  </main>
</body>
</html>
```